Introduction Post card

Harbourline Doors
27 Varnel Road
Ruthven Ontario
Gus@harbourlinedoorsco.net
519-555-0143

Dear Leamington Residents

We are excited to announce the launch of Harbourline Doors, your new local source for high-quality windows, doors, and garage doors! As a dedicated member of this community, we are committed to providing exceptional products and services that enhance the beauty and functionality of your home or business.

At Harbourline Doors, we understand that choosing the right windows and doors is essential for energy efficiency, security, and style. That’s why we offer a wide selection of premium products tailored to meet your unique needs. Our expert team is here to guide you through the selection process, ensuring you find the perfect fit for your space.

Our services don’t stop at providing quality products. We pride ourselves on our professional installation process, ensuring that every project is completed with precision and care. Customer satisfaction is our top priority, and we strive to exceed your expectations with every interaction.

We invite you to visit our showroom or contact us to learn more about our offerings. Whether you’re looking to upgrade your home’s curb appeal or enhance its security, we are here to help. Together, let’s make our community a more beautiful place!

Thank you for considering Harbourline Doors for your window, door, and garage door needs. We look forward to serving you!

Warm regards,

Gus
Sales Manager
Harbourline Doors
https://harbourlinedoorsco.net/

```html
<!DOCTYPE html>
<html lang="en">
<head>
<meta charset="utf-8">
<title>Harbourline Doors – Introduction Postcard</title>
<link href="https://fonts.googleapis.com/css2?family=Montserrat:wght@500;600;700;800&family=Barlow:wght@400;600&family=Great+Vibes&display=swap" rel="stylesheet">
<style>
  :root{
    --stage:#a7a7a7;
    --charcoal:#262626;
    --charcoal-soft:#3a3a3a;
    --orange:#e9592a;
    --orange-deep:#c8420f;
    --orange-light:#f6a06a;
    --white:#ffffff;
    --ink:#1e1e1e;
    --rule:#8a8a8a;
    --stamp:#d9d9d9;
  }
  *{margin:0;padding:0;box-sizing:border-box}
  html,body{width:888px;height:1200px;overflow:hidden}
  body{background:var(--stage);position:relative;font-family:"Montserrat",sans-serif;color:var(--ink)}
  .card{position:absolute;left:101px;width:686px;height:490px;overflow:hidden;background:var(--white)}
  .card--front{top:88px}
  .card--back{top:623px}
  .abs{position:absolute}

  /* FRONT */
  .front-hero{left:0;top:0;width:686px;height:318px;background:linear-gradient(100deg,#222 0%,#2e2e2e 45%,#3b3b3b 100%)}
  .brand{display:flex;align-items:center;gap:8px}
  .brand__mark{width:30px;height:30px;border:3px solid var(--white)}
  .brand__name{font-weight:700;font-size:17px;color:var(--orange);letter-spacing:.2px}
  .front-brand{left:37px;top:37px}
  .greeting{left:37px;top:115px;width:258px;height:31px;background:var(--orange);border-radius:0 10px 10px 0;border-left:3px solid var(--white);display:flex;align-items:center;padding-left:8px;color:var(--white);gap:5px}
  .greeting__hello{font-family:"Great Vibes",cursive;font-size:23px}
  .greeting__place{font-weight:700;font-size:11px;letter-spacing:1.3px}
  .intro-script{left:37px;top:148px;font-family:"Great Vibes",cursive;font-size:42px;color:var(--orange)}
  .headline{left:37px;top:196px;font-weight:800;font-size:36px;line-height:38px;color:var(--white)}
  .tagline{left:38px;top:277px;font-weight:700;font-size:17px;color:var(--white)}
  .tagline em{font-style:normal;color:var(--orange)}
  .band{left:0;top:318px;width:686px;height:43px;background:var(--orange)}
  .band__text{left:37px;top:329px;font-weight:700;font-size:13.5px;color:var(--white)}
  .services{left:308px;top:305px;width:345px;height:56px;background:var(--orange-deep)}
  .service-label{top:334px;width:106px;text-align:center;font-weight:700;font-size:13px;color:var(--white)}
  .hero-frame{left:345px;top:37px;width:304px;height:210px;border-radius:22px;background:linear-gradient(135deg,var(--orange) 0%,var(--orange-light) 100%)}
  .hero-photo{left:355px;top:46px;width:285px;height:198px;border-radius:18px;background:linear-gradient(180deg,#3c5a7a 0%,#2f3f5a 45%,#3f6b2c 80%,#2f5222 100%)}
  .thumb{top:244px;width:106px;height:77px;border-radius:8px;border:2px solid var(--white)}
  .thumb--garage{left:311px;background:linear-gradient(180deg,#8aa5c4 0%,#6b5a4a 60%,#4a5a3a 100%)}
  .thumb--windows{left:427px;background:linear-gradient(180deg,#e9ecef 0%,#d4d0ca 60%,#b9a592 100%)}
  .thumb--doors{left:543px;background:linear-gradient(90deg,#cfd2d4 0%,#c85a8a 18%,#2a2a2a 40%,#2a2a2a 60%,#c85a8a 82%,#cfd2d4 100%)}

  .cta{left:37px;top:385px;width:230px;height:29px;display:flex}
  .cta__label{flex:1;background:var(--charcoal);border-radius:15px 0 0 15px;color:var(--white);font-weight:700;font-size:15.5px;display:flex;align-items:center;padding-left:14px}
  .cta__arrow{width:30px;margin-left:2px;background:var(--orange);color:var(--white);font-weight:700;font-size:12px;display:flex;align-items:center;justify-content:center}
  .cta-sub{left:37px;top:416px;font-weight:500;font-size:15.5px;line-height:19px}
  .cta-sub strong{color:var(--orange);font-weight:700}
  .divider{top:389px;height:64px;border-left:1px dashed #555}
  .icon{width:14px;height:14px}
  .addr{left:305px;top:391px;display:flex;gap:7px}
  .addr__text{font-weight:500;font-size:12px;line-height:14.5px}
  .addr__name{color:var(--orange);font-weight:700}
  .contacts{left:478px;top:391px;display:flex;flex-direction:column;gap:5px}
  .contacts__row{display:flex;align-items:center;gap:7px;font-weight:500;font-size:12px;line-height:14.5px}

  /* BACK */
  .letter{left:0;top:0;width:389px;height:490px;background:linear-gradient(160deg,#2a2a2a 0%,#232323 55%,#303030 100%)}
  .letter__dear{left:37px;top:30px;font-family:"Great Vibes",cursive;font-size:36px;color:var(--white)}
  .letter__to{left:37px;top:68px;font-weight:700;font-size:17px;color:var(--orange)}
  .letter__body{left:37px;top:102px;width:300px;font-family:"Barlow",sans-serif;font-size:8.8px;line-height:11.3px;color:var(--white)}
  .letter__body p{margin-bottom:10.2px}
  .letter__body .closing{font-weight:600}
  .letter__regards{left:37px;top:382px;font-family:"Great Vibes",cursive;font-size:22px;color:var(--white)}
  .signature{left:37px;top:412px;font-weight:700;font-size:11px;line-height:13.2px;color:var(--orange)}
  .web-pill{left:160px;top:431px;width:238px;height:23px;background:var(--orange);border-radius:12px 0 0 12px;color:var(--white);font-weight:600;font-size:11.5px;letter-spacing:1.9px;display:flex;align-items:center;justify-content:center}
  .back-brand{left:411px;top:40px}
  .back-brand .brand__mark{width:26px;height:26px}
  .back-brand .brand__name{font-size:12px}
  .return-addr{left:413px;top:80px;font-size:9.5px;line-height:11.3px;font-weight:500}
  .return-contact{left:413px;top:120px;font-size:9.5px;line-height:13.5px;font-weight:500}
  .return-contact span{color:var(--orange);font-size:8px;margin-right:3px}
  .stamp{left:585px;top:38px;width:64px;height:64px;border-radius:5px;background:var(--stamp)}
  .addr-line{left:413px;width:237px;border-top:1px solid var(--rule)}
</style>
</head>
<body>

<section class="card card--front" aria-label="Postcard front">
  <div class="abs front-hero" role="img" aria-label="Dark faded photo of a house at dusk"></div>

  <div class="abs brand front-brand">
    <span class="brand__mark"></span>
    <span class="brand__name">Harbourline Doors</span>
  </div>

  <div class="abs greeting"><span class="greeting__hello">Hello</span><span class="greeting__place">LEAMINGTON RESIDENTS</span></div>
  <div class="abs intro-script">Introducing</div>
  <h1 class="abs headline">HARBOURLINE<br>DOORS</h1>
  <div class="abs tagline"><em>Your Trusted</em> Local Source</div>

  <div class="abs hero-frame"></div>
  <div class="abs hero-photo" role="img" aria-label="Photo of a blue two-storey house with lit windows and a green lawn at dusk"></div>

  <div class="abs band"></div>
  <div class="abs band__text">New local source for High-Quality</div>
  <div class="abs services"></div>
  <div class="abs thumb thumb--garage" role="img" aria-label="Photo of a stone house with a garage door"></div>
  <div class="abs thumb thumb--windows" role="img" aria-label="Photo of a bright bedroom with large windows"></div>
  <div class="abs thumb thumb--doors" role="img" aria-label="Photo of a black front door framed by columns and flowers"></div>
  <div class="abs service-label" style="left:311px">Garage Door</div>
  <div class="abs service-label" style="left:427px">Windows</div>
  <div class="abs service-label" style="left:543px">Doors</div>

  <div class="abs cta"><span class="cta__label">Visit our showroom</span><span class="cta__arrow">&gt;</span></div>
  <p class="abs cta-sub">Or contact us to learn more<br><strong>about our offerings</strong></p>

  <div class="abs divider" style="left:291px"></div>
  <div class="abs addr">
    <svg class="icon" viewBox="0 0 14 14"><circle cx="7" cy="7" r="7" fill="var(--orange)"/><path d="M7 3.2a2.4 2.4 0 0 0-2.4 2.4c0 1.8 2.4 4.4 2.4 4.4s2.4-2.6 2.4-4.4A2.4 2.4 0 0 0 7 3.2z" fill="#fff"/><circle cx="7" cy="5.6" r=".9" fill="var(--orange)"/></svg>
    <div class="addr__text"><span class="addr__name">Harbourline Doors</span><br>27 Varnel Road<br>Ruthven<br>Ontario</div>
  </div>

  <div class="abs divider" style="left:455px"></div>
  <div class="abs contacts">
    <div class="contacts__row">
      <svg class="icon" viewBox="0 0 14 14"><circle cx="7" cy="7" r="7" fill="var(--orange)"/><path d="M4.6 3.6l1.3 1.5-.7.9a5 5 0 0 0 2.8 2.8l.9-.7 1.5 1.3-.8 1.1C6.6 10.4 3.6 7.4 3.5 4.4z" fill="#fff"/></svg>
      519-555-0143
    </div>
    <div class="contacts__row">
      <svg class="icon" viewBox="0 0 14 14"><circle cx="7" cy="7" r="7" fill="var(--orange)"/><rect x="3.5" y="4.5" width="7" height="5" fill="#fff"/><path d="M3.5 4.5L7 7.3l3.5-2.8" fill="none" stroke="var(--orange)" stroke-width=".8"/></svg>
      Gus@harbourlinedoorsco.net
    </div>
    <div class="contacts__row">
      <svg class="icon" viewBox="0 0 14 14"><circle cx="7" cy="7" r="7" fill="var(--orange)"/><circle cx="7" cy="7" r="3.4" fill="none" stroke="#fff" stroke-width=".9"/><path d="M3.6 7h6.8M7 3.6c-1.5 2-1.5 4.8 0 6.8M7 3.6c1.5 2 1.5 4.8 0 6.8" fill="none" stroke="#fff" stroke-width=".7"/></svg>
      www.harbourlinedoorsco.net
    </div>
  </div>
</section>

<section class="card card--back" aria-label="Postcard back">
  <div class="abs letter" role="img" aria-label="Dark faded photo of a house behind the letter"></div>
  <div class="abs letter__dear">Dear</div>
  <h2 class="abs letter__to">Leamington Residents</h2>
  <div class="abs letter__body">
    <p>We are excited to announce the launch of Harbourline Doors, your new local source for high-quality windows, doors, and garage doors! As a dedicated member of this community, we are committed to providing exceptional products and services that enhance the beauty and functionality of your home or business.</p>
    <p>At Harbourline Doors, we understand that choosing the right windows and doors is essential for energy efficiency, security, and style. That’s why we offer a wide selection of premium products tailored to meet your unique needs. Our expert team is here to guide you through the selection process, ensuring you find the perfect fit for your space.</p>
    <p>Our services don’t stop at providing quality products. We pride ourselves on our professional installation process, ensuring that every project is completed with precision and care. Customer satisfaction is our top priority, and we strive to exceed your expectations with every interaction.</p>
    <p>We invite you to visit our showroom or contact us to learn more about our offerings. Whether you’re looking to upgrade your home’s curb appeal or enhance its security, we are here to help. Together, let’s make our community a more beautiful place!</p>
    <p class="closing">Thank you for considering Harbourline Doors for your window, door, and garage door needs. We look forward to serving you!</p>
  </div>
  <div class="abs letter__regards">Warm regards,</div>
  <div class="abs signature">Gus<br>Sales Manager<br>Harbourline Doors</div>
  <div class="abs web-pill">www.harbourlinedoorsco.net</div>

  <div class="abs brand back-brand">
    <span class="brand__mark"></span>
    <span class="brand__name">Harbourline Doors</span>
  </div>
  <div class="abs return-addr">Harbourline Doors<br>27 Varnel Road<br>Ruthven Ontario</div>
  <div class="abs return-contact"><span>&#9742;</span>519-555-0143<br><span>&#9993;</span>Gus@harbourlinedoorsco.net</div>
  <div class="abs stamp"></div>
  <div class="abs addr-line" style="top:275px"></div>
  <div class="abs addr-line" style="top:311px"></div>
  <div class="abs addr-line" style="top:347px"></div>
</section>

</body>
</html>
```